Eye-catching Card for new church

I would like a card the size of a business card ... that can be used to announce the start of our new church. I would like it to have our logo on the card, my name, and the statement "Coming Soon ... 1.10.2016". I also would like to list our website address and Facebook page and my Twitter account.

Target Market(s)

prospective people looking for a church

Industry/Entity Type

Church

Requirements
Must have
• a focus on Coming Soon ... 1.10.2016
• Brightfold Church logo
Should not have
• church buildings or writings on the cross

```html
<!DOCTYPE html>
<html lang="en">
<head>
<meta charset="utf-8">
<title>Brightfold Church – Coming Soon Card</title>
<link rel="stylesheet" href="https://fonts.googleapis.com/css2?family=Nunito+Sans:ital,wght@0,400;0,700;0,800;1,800&display=swap">
<style>
  :root {
    --page-bg: #e9ebee;
    --card-white: #ffffff;
    --blue-deep: #283a97;
    --blue-mid: #1b7cc6;
    --blue-light: #4ec7f1;
    --ink-dark: #3a3d44;
    --text-light: #ffffff;
    --shadow-blue: #1b3f8f;
  }
  * { box-sizing: border-box; margin: 0; padding: 0; }
  html, body {
    width: 1200px; height: 1000px; overflow: hidden;
    background: var(--page-bg);
    font-family: "Nunito Sans", Arial, sans-serif;
  }
  .business-card {
    position: absolute; left: 390px; top: 120px;
    width: 420px; height: 760px;
    border-radius: 26px; overflow: hidden;
    background: var(--card-white);
    box-shadow: 0 18px 40px rgba(0,0,0,0.18);
  }
  .card-header {
    height: 270px;
    display: flex; flex-direction: column; align-items: center; justify-content: center;
    gap: 14px;
  }
  .church-mark {
    width: 64px; height: 64px; border-radius: 50%;
    background: var(--blue-mid);
  }
  .church-name {
    font-weight: 700; font-size: 34px; letter-spacing: 3px;
    color: var(--ink-dark); text-transform: uppercase; text-align: center; line-height: 1.1;
  }
  .card-body {
    height: 490px;
    background: linear-gradient(180deg, var(--blue-deep) 0%, var(--blue-mid) 45%, var(--blue-light) 100%);
    color: var(--text-light);
    padding: 34px 34px 0;
    position: relative;
  }
  .pastor-name {
    display: flex; align-items: center; gap: 14px;
    font-weight: 800; font-size: 36px; white-space: nowrap;
  }
  .pastor-name::before, .pastor-name::after {
    content: ""; flex: 1; height: 2px; background: var(--text-light);
  }
  .contact-list { list-style: none; margin-top: 42px; display: grid; gap: 36px; }
  .contact-item { display: flex; align-items: center; gap: 14px; font-size: 22px; }
  .contact-icon { width: 24px; height: 24px; flex: none; }
  .announcement {
    position: absolute; left: 34px; right: 20px; bottom: 50px;
    font-weight: 800; font-style: italic; font-size: 32px; white-space: nowrap;
    text-shadow: 2px 3px 0 var(--shadow-blue);
  }
</style>
</head>
<body>
  <article class="business-card">
    <header class="card-header">
      <span class="church-mark"></span>
      <div class="church-name">Brightfold<br>Church</div>
    </header>
    <section class="card-body">
      <h1 class="pastor-name">Daniel Carver</h1>
      <ul class="contact-list">
        <li class="contact-item">
          <svg class="contact-icon" viewBox="0 0 24 24" fill="none" stroke="#fff" stroke-width="2">
            <circle cx="12" cy="12" r="10"/><ellipse cx="12" cy="12" rx="4.5" ry="10"/>
            <line x1="2" y1="12" x2="22" y2="12"/><line x1="4" y1="7" x2="20" y2="7"/><line x1="4" y1="17" x2="20" y2="17"/>
          </svg>
          <span>thebrightfoldchurch.com</span>
        </li>
        <li class="contact-item">
          <svg class="contact-icon" viewBox="0 0 24 24"><rect x="1" y="1" width="22" height="22" rx="3" fill="#fff"/></svg>
          <span>BrightfoldChurchFM</span>
        </li>
        <li class="contact-item">
          <svg class="contact-icon" viewBox="0 0 24 24"><circle cx="12" cy="12" r="11" fill="#fff"/></svg>
          <span>@CarverDn</span>
        </li>
      </ul>
      <p class="announcement">Coming Soon ... 1.10.16</p>
    </section>
  </article>
</body>
</html>
```